New travel store signage for our 2nd Mellow Journeys store to attract luxury travellers

Hello,

We had the attached signage created for our new branch but we are now looking to update our other branch to have new signage. This new sign must have the same colors and same design as the first graphic but it requires new information.

The top sign must include:
1. Sailing Beside Mellow Journeys Logo(attached)
2. The text...www.sailingbesidemellowjourneys.example
3. The text ... Specialists in Ocean, River, Exploration & Yacht-style Cruise Holidays
4. Brand Colours ( Fb0196, 412266, d41d84 and ffffff)

The bottom sign must include:
1. Mellow Journeys Outings Logo(attached)
2. The text...www.mellowjourneysoutings.example
3. The text ... Specialists in Day Trips, Theatre Trips, Short Breaks and More!

These new signs must match the design that was created in the first design and have the same colours and curve as your first design

Thank you

Target Market(s)

Retail

Industry/Entity Type

Travel Agency

Font styles to use
Other font styles liked:
• Radley

Colors
E54698
E96AAD
F1A4CE
F9D9EA
FCEFF6
A7469A
B969AE
D3A5CF
EDDBEB
F8F0F9

Requirements
Must have
• The top sign must include: 1. Sailing Beside Mellow Journeys Logo(attached) 2. The text...www.sailingbesidemellowjourneys.example 3. The text ... Specialists in Ocean, River, Exploration & Yacht-style Cruise Holidays 4. Brand Colours ( Fb0196, 412266, d41d84 and ffffff) The bottom sign must include: 1. Mellow Journeys Outings Logo(attached) 2. The text...www.mellowjourneysoutings.example 3. The text ... Specialists in Day Trips, Theatre Trips, Short Breaks and More! 4. Brand Colours ( Fb0196, 412266, d41d84 and ffffff)

```html
<!DOCTYPE html>
<html lang="en">
<head>
<meta charset="utf-8">
<title>Mellow Journeys Store Signage</title>
<link href="https://fonts.googleapis.com/css2?family=Radley&display=swap" rel="stylesheet">
<style>
  :root {
    --purple: #412266;
    --pink: #fb0196;
    --pink-deep: #d41d84;
    --white: #ffffff;
    --backdrop: #e2e2e2;
  }
  * { margin: 0; padding: 0; box-sizing: border-box; }
  html, body {
    width: 1200px;
    height: 347px;
    overflow: hidden;
    background: var(--backdrop);
  }
  .canvas {
    position: relative;
    width: 1200px;
    height: 347px;
  }
  .sign {
    position: absolute;
    left: 46px;
    width: 1108px;
    font-family: "Radley", Georgia, serif;
    color: var(--white);
  }
  .sign--cruise { top: 40.5px; height: 78.4px; }
  .sign--outings { top: 202px; height: 74px; }
  .sign__art {
    position: absolute;
    inset: 0;
    width: 100%;
    height: 100%;
    display: block;
  }
  .sign__identity {
    position: absolute;
    width: 150px;
    text-align: center;
    white-space: nowrap;
    line-height: 1;
    font-family: "Radley", Georgia, serif;
  }
  .sign--cruise .sign__identity { left: 158px; top: 8px; }
  .sign--outings .sign__identity { left: 159px; top: 6px; }
  .sign__brand {
    font-size: 13px;
    line-height: 1.05;
  }
  .sign--cruise .sign__brand { color: var(--pink-deep); }
  .sign--outings .sign__brand { color: var(--purple); }
  .sign__web {
    margin-top: 3px;
    font-size: 8.5px;
    color: var(--purple);
    letter-spacing: 0.1px;
  }
  .sign__title {
    position: absolute;
    font-weight: 400;
    white-space: nowrap;
    line-height: 1;
  }
  .sign--cruise .sign__title { left: 403px; top: 6px; font-size: 33px; }
  .sign--outings .sign__title { left: 410px; top: 5px; font-size: 34px; }
  .sign__tagline {
    position: absolute;
    font-size: 14.6px;
    white-space: nowrap;
    line-height: 1;
  }
  .sign--cruise .sign__tagline { left: 403px; top: 42px; }
  .sign--outings .sign__tagline { left: 410px; top: 41px; }
</style>
</head>
<body>
<main class="canvas">

  <section class="sign sign--cruise">
    <svg class="sign__art" viewBox="0 0 1108 78.4" preserveAspectRatio="none" aria-hidden="true">
      <rect width="1108" height="78.4" fill="var(--white)"/>
      <rect width="1108" height="72" fill="var(--purple)"/>
      <path d="M0,0 L317.7,0 Q346,26 358,72 L0,72 Z" fill="var(--white)"/>
      <path d="M0,53.3 Q553,94.3 1108,55.3 L1108,78.4 L0,78.4 Z" fill="var(--white)"/>
      <path d="M0,29.7 Q553,104 1108,33.8 L1108,55.3 Q553,94.3 0,53.3 Z" fill="var(--pink)"/>
      <path d="M0,53.3 Q553,94.3 1108,55.3" fill="none" stroke="var(--purple)" stroke-width="0.9"/>
      <path d="M0,69.7 Q553,82.9 1108,69.7 L1108,78.4 L0,78.4 Z" fill="var(--purple)"/>
    </svg>
    <div class="sign__identity">
      <p class="sign__brand">Sailing Beside<br>Mellow Journeys</p>
      <p class="sign__web">www.sailingbesidemellowjourneys.example</p>
    </div>
    <h2 class="sign__title">Sailing Beside Mellow Journeys</h2>
    <p class="sign__tagline">Specialists in Ocean, River, Exploration &amp; Yacht-style Cruise Holidays</p>
  </section>

  <section class="sign sign--outings">
    <svg class="sign__art" viewBox="0 0 1108 74" preserveAspectRatio="none" aria-hidden="true">
      <rect width="1108" height="74" fill="var(--white)"/>
      <rect width="1108" height="68" fill="var(--purple)"/>
      <path d="M0,0 L320,0 Q346,24 356,68 L0,68 Z" fill="var(--white)"/>
      <path d="M0,48.7 Q553,85.7 1108,52.3 L1108,74 L0,74 Z" fill="var(--white)"/>
      <path d="M0,27.7 Q553,98 1108,31.8 L1108,52.3 Q553,85.7 0,48.7 Z" fill="var(--pink)"/>
      <path d="M0,48.7 Q553,85.7 1108,52.3" fill="none" stroke="var(--purple)" stroke-width="0.9"/>
      <path d="M0,65 Q553,77.4 1108,65 L1108,74 L0,74 Z" fill="var(--purple)"/>
    </svg>
    <div class="sign__identity">
      <p class="sign__brand">Mellow Journeys<br>Outings</p>
      <p class="sign__web">www.mellowjourneysoutings.example</p>
    </div>
    <h2 class="sign__title">Mellow Journeys Outings</h2>
    <p class="sign__tagline">Specialists in Day Trips, Theatre Trips, Short Breaks and More!</p>
  </section>

</main>
</body>
</html>
```